Skylark Air Works Logo

I need a website and logo for the parent company Skylark Air Works, which encompasses general aviation aircraft repair, small aircrat rental and flight school. The company is based in Lawrenceville, Georgia at the Brookhollow county airfield. A saying that can be incorporated somehere could be, "Quality flying is safe flying", "Safety in mind is no accident" ,. I need a website and logo.

The company started as a repair shop performing repairs and inspections on Halvorn, Tamsel, Korvane and Drexley general aviation aircraft, all models of single engine piston, multi engine piston, and single engine turboprop with an emphasis on Halvorn Solstice and AeroKite turbo prop aircraft. We have se=ince entered the aircraft rental and flight instruction market using the Korvane 418 ang Halvorn Ranger aircraft.

Number of Pages; I don't know. Maybe 5 ? A home page for Skylark Air Works, page for maintenance and repairs and a couple for the rental and school. The maintenance shop is busy, always has been. I need to get the rental and school advertised and busy.

I have a logo for the maintenance shop shirts, not for the school. I do not have the file. I paid a business locally to do that and print on the shirts. They have the file.

Target Market(s)

In our flight school rental fleet department, we are looking for persons wishing to obtain their private pilot license and continuing on into their commercial and instrument ratings. In the aircraft maintenance department, we are looking for new customers who want a better and more quality relationship with their aircraft maintenance provider who will give more detail and quality in the repairs with an emphasis on safety and fewer problems between scheduled maintenance cycles on their aircraft. Skylark's owner, Dale Fenwick, has been performing aircraft maintenance in the Atlanta area for 27 years. He has built a steady customer base through those years.

```html
<!DOCTYPE html>
<html lang="en">
<head>
<meta charset="utf-8">
<title>Skylark Air Works</title>
<link href="https://fonts.googleapis.com/css2?family=Libre+Caslon+Text:wght@400&family=Poppins:wght@400;500;600;700&display=swap" rel="stylesheet">
<style>
:root{
  --gold:#b39a0c;
  --gold-dark:#9c8508;
  --navy:#1f1f5e;
  --navy-deep:#1a1a4f;
  --ink:#1d1d3a;
  --text:#6f6f7a;
  --mist:#ececf1;
  --white:#ffffff;
  --serif:"Libre Caslon Text", Georgia, serif;
  --sans:"Poppins", Arial, sans-serif;
}
*{margin:0;padding:0;box-sizing:border-box}
html,body{width:1200px;height:3997px;overflow:hidden;background:var(--white);font-family:var(--sans);color:var(--text)}
.page{position:relative;width:1200px;height:3997px;overflow:hidden}
.abs{position:absolute}
.label{position:absolute;font:600 11px/1 var(--sans);color:var(--gold);text-transform:uppercase;letter-spacing:.3px}
.heading{position:absolute;font:400 30px/38px var(--serif);color:var(--ink)}
.center{left:0;width:1200px;text-align:center}
.btn{position:absolute;display:flex;align-items:center;justify-content:center;border-radius:20px;font:600 11.5px/1 var(--sans);color:var(--white);background:var(--gold)}
.btn.light{background:var(--white);color:var(--navy)}
.arrows{position:absolute;display:flex;gap:14px}
.arrows svg{width:22px;height:12px}
.photo{position:absolute}

/* hero */
.hero{position:absolute;left:0;top:0;width:1200px;height:636px;background:linear-gradient(180deg,#4b3f72 0%,#7a5d78 30%,#8d6a5c 45%,#3f4a3a 70%,#2e3427 100%)}
.hero-shade{position:absolute;inset:0;background:linear-gradient(90deg,rgba(20,18,40,.55),rgba(20,18,40,0) 60%)}
.brand{position:absolute;display:flex;align-items:center;gap:10px;font:400 24px/1 var(--serif);color:var(--white);letter-spacing:.5px}
.brand i{display:block;width:14px;height:14px;border-radius:50%;background:var(--gold)}
.nav{position:absolute;left:461px;top:24px;font:500 11.5px/1 var(--sans);color:var(--white)}
.nav span{position:absolute;white-space:nowrap}
.hero-title{position:absolute;left:113px;top:342px;font:400 39px/48px var(--serif);color:var(--white);letter-spacing:.5px}
.hero-copy{position:absolute;left:113px;top:442px;width:372px;font:400 11.5px/19px var(--sans);color:var(--white)}
.social{position:absolute;top:523px;width:18px;height:18px;border-radius:50%;background:var(--gold)}

/* about */
.check{display:inline-block;width:15px;height:15px;border-radius:50%;background:var(--gold);position:absolute}
.check svg{position:absolute;left:3px;top:3px}
.feat-title{position:absolute;font:600 11.5px/15px var(--sans);color:var(--ink)}
.feat-copy{position:absolute;font:400 11.5px/15px var(--sans);color:var(--text)}

/* features */
.feature{position:absolute;top:1288px;height:173px;background:var(--white);box-shadow:0 6px 18px rgba(30,30,80,.07)}
.feature svg{position:absolute;left:19px;top:32px}
.feature h3{position:absolute;left:19px;top:80px;font:600 11.5px/14px var(--sans);color:var(--ink);text-transform:uppercase}
.feature p{position:absolute;left:19px;top:112px;width:150px;font:400 11.5px/14px var(--sans);color:var(--text)}
.feature.active{background:var(--gold)}
.feature.active h3,.feature.active p{color:var(--white)}

/* fleet */
.charter{position:absolute;top:1870px;height:346px;overflow:hidden}
.charter .panel{position:absolute;left:19px;top:137px;width:170px;height:192px;background:var(--white)}
.charter .tag{position:absolute;left:0;top:0;width:170px;height:36px;background:var(--gold);color:var(--white);font:600 11.5px/36px var(--sans);padding-left:18px}
.charter ul{position:absolute;left:18px;top:50px;list-style:none;font:400 9.5px/18.5px var(--sans);color:#9a9aa6;white-space:nowrap}
.charter b{color:var(--ink);font-weight:600}

/* form */
.field{position:absolute;height:70px;background:var(--white);font:400 11.5px/70px var(--sans);color:var(--ink);padding-left:24px}
.field svg{position:absolute;right:22px;top:30px}

/* testimonials */
.review{position:absolute;top:2879px;width:321px;height:182px;background:var(--white)}
.avatar{position:absolute;left:17px;top:-22px;width:68px;height:68px;border-radius:50%;border:4px solid var(--white)}
.review h4{position:absolute;left:97px;top:36px;font:600 12px/1 var(--sans);color:var(--ink)}
.review small{position:absolute;left:97px;top:51px;font:500 8.5px/1 var(--sans);color:var(--gold);text-transform:uppercase}
.review p{position:absolute;left:31px;top:68px;width:262px;font:400 11px/19px var(--sans);color:var(--text)}
.quote{position:absolute;right:12px;top:-22px;font:700 74px/1 var(--serif);color:var(--gold)}
.stars{position:absolute;left:31px;top:150px;display:flex;gap:5px}

/* blog */
.post{position:absolute;top:3295px;width:262px;height:383px;background:var(--white);box-shadow:0 6px 18px rgba(30,30,80,.08)}
.post .pill{position:absolute;left:19px;top:225px;width:56px;height:20px;border-radius:10px;background:var(--gold);color:var(--white);font:500 9px/20px var(--sans);text-align:center}
.post .meta{position:absolute;left:19px;top:261px;display:flex;gap:16px;font:400 9px/12px var(--sans);color:#9a9aa6;align-items:center}
.post .meta span{display:flex;align-items:center;gap:6px}
.post h3{position:absolute;left:19px;top:282px;width:200px;font:600 13.5px/19px var(--sans);color:var(--navy)}
.post .more{position:absolute;right:27px;top:350px;display:flex;align-items:center;gap:10px;font:400 11px/1 var(--sans);color:#8a8a96}

/* footer */
.footer{position:absolute;left:0;top:3731px;width:1200px;height:266px;background:var(--navy-deep)}
.footer h5{position:absolute;font:500 14px/1 var(--sans);color:var(--white)}
.footer ul{position:absolute;list-style:none;font:400 11.5px/19px var(--sans);color:var(--white);white-space:nowrap}
.footer li{display:flex;align-items:center;gap:10px}
</style>
</head>
<body>
<div class="page">

<!-- HERO -->
<section class="hero">
  <div role="img" aria-label="Small propeller aircraft parked on a grass airfield at sunset" style="position:absolute;inset:0"></div>
  <div class="hero-shade"></div>
  <div class="brand" style="left:113px;top:48px"><i></i>SKYLARK AIR WORKS</div>
  <nav class="nav">
    <span style="left:0;color:var(--gold)">Home</span>
    <span style="left:68px">About Us</span>
    <span style="left:150px">Repairs</span>
    <span style="left:222px">Rental</span>
    <span style="left:285px">School</span>
    <span style="left:352px">Contact Us</span>
    <svg style="position:absolute;left:446px;top:-2px" width="15" height="15" viewBox="0 0 15 15" fill="none" stroke="#fff" stroke-width="1.4"><circle cx="6.5" cy="6.5" r="5"/><path d="M10 10l4 4"/></svg>
  </nav>
  <div class="btn" style="left:964px;top:16px;width:122px;height:31px;border-radius:16px">Book Now</div>
  <h1 class="hero-title">QUALITY FLYING<br>IS SAFE FLYING</h1>
  <p class="hero-copy">Skylark Air Works keeps general aviation aircraft flying safely with careful repairs and inspections, plus rental aircraft and flight training.</p>
  <div class="btn" style="left:113px;top:517px;width:121px;height:31px;background:transparent;border:1.5px solid var(--gold)">Book a Lesson</div>
  <div class="abs" style="left:267px;top:527px;display:flex;align-items:center;gap:8px;font:600 11.5px/1 var(--sans);color:#fff">Request Quote
    <svg width="22" height="10" viewBox="0 0 22 10" fill="none" stroke="#fff" stroke-width="1.3"><path d="M0 5h20M16 1l4 4-4 4"/></svg></div>
  <span class="social" style="left:866px"></span>
  <span class="social" style="left:896px"></span>
  <span class="social" style="left:925px"></span>
  <span class="social" style="left:954px"></span>
  <div class="abs" style="left:984px;top:532px;width:216px;height:1px;background:rgba(255,255,255,.6)"></div>
</section>

<!-- ABOUT -->
<section>
  <div class="photo" role="img" aria-label="Pilot at an airfield window watching a plane" style="left:112px;top:677px;width:302px;height:310px;background:linear-gradient(160deg,#9fb8d4,#c9cbd1 55%,#6f6258)"></div>
  <div class="photo" role="img" aria-label="Aircraft parked inside a maintenance hangar" style="left:306px;top:784px;width:302px;height:309px;background:linear-gradient(180deg,#4f4f52,#8b8a86 50%,#3b3b3d)"></div>
  <div class="abs" style="left:329px;top:854px;width:62px;height:62px;border-radius:50%;background:#fff"></div>
  <svg class="abs" style="left:352px;top:873px" width="20" height="24" viewBox="0 0 20 24"><path d="M0 0l20 12L0 24z" fill="#111"/></svg>

  <div class="label" style="left:691px;top:721px">About Skylark Air Works</div>
  <h2 class="heading" style="left:691px;top:740px">Experience quality<br>care for your aircraft</h2>
  <p class="abs" style="left:691px;top:828px;width:390px;font:500 11.5px/18px var(--sans);color:var(--gold)">Safety in mind is no accident. Our owner brings 27 years of aircraft maintenance in the Atlanta area.</p>
  <p class="abs" style="left:691px;top:884px;width:390px;font:400 11.5px/19px var(--sans);color:var(--text)">We repair and inspect single and multi engine piston and turboprop aircraft, with extra detail that means fewer problems between scheduled maintenance.</p>
  <span class="check" style="left:691px;top:962px"><svg width="9" height="9" viewBox="0 0 9 9" fill="none" stroke="#fff" stroke-width="1.6"><path d="M1 4.5l2.3 2.3L8 2"/></svg></span>
  <div class="feat-title" style="left:715px;top:961px">Detailed repairs</div>
  <div class="feat-copy" style="left:715px;top:980px">Piston and turboprop.</div>
  <span class="check" style="left:897px;top:962px"><svg width="9" height="9" viewBox="0 0 9 9" fill="none" stroke="#fff" stroke-width="1.6"><path d="M1 4.5l2.3 2.3L8 2"/></svg></span>
  <div class="feat-title" style="left:921px;top:961px">Certified instructors</div>
  <div class="feat-copy" style="left:921px;top:980px">Private to commercial.</div>
  <div class="btn" style="left:691px;top:1016px;width:122px;height:32px">Book Now</div>
</section>

<!-- FEATURES -->
<section>
  <div class="abs" style="left:0;top:1133px;width:1200px;height:248px;background:var(--mist)"></div>
  <div class="label center" style="top:1173px">Our Services</div>
  <h2 class="heading center" style="top:1192px">Why owners and students<br>choose Skylark</h2>

  <div class="feature" style="left:183px;width:196px">
    <svg width="30" height="32" viewBox="0 0 30 32" fill="none" stroke="#b39a0c" stroke-width="1.5"><rect x="3" y="4" width="24" height="27" rx="2"/><rect x="10" y="1" width="10" height="6" rx="1"/><path d="M8 14l2 2 4-4M17 14h6M8 22l2 2 4-4M17 22h6"/></svg>
    <h3>Detailed<br>inspections</h3><p>Thorough checks on every airframe</p>
  </div>
  <div class="feature active" style="left:397px;width:193px">
    <svg width="30" height="32" viewBox="0 0 30 32" fill="none" stroke="#fff" stroke-width="1.6"><path d="M15 2l12 4v9c0 8-6 13-12 15C9 28 3 23 3 15V6z"/><path d="M9 16l4 4 8-8"/></svg>
    <h3>Safety<br>first</h3><p>Quality flying is safe flying</p>
  </div>
  <div class="feature" style="left:610px;width:192px">
    <svg width="30" height="30" viewBox="0 0 30 30" fill="none" stroke="#b39a0c" stroke-width="1.5"><rect x="2" y="4" width="26" height="24" rx="2"/><path d="M2 10h26M8 1v6M22 1v6"/><path d="M7 15h3M13.5 15h3M20 15h3M7 20h3M13.5 20h3M20 20h3M7 24h3M13.5 24h3"/></svg>
    <h3>Flexible<br>schedules</h3><p>Lessons and rentals that fit your week</p>
  </div>
  <div class="feature" style="left:823px;width:192px">
    <svg width="34" height="30" viewBox="0 0 34 30" fill="none" stroke="#b39a0c" stroke-width="1.5"><path d="M4 28V12h14v16M18 28V6h12v22M2 28h30"/><path d="M8 16h6M8 21h6M22 11h4M22 16h4M22 21h4"/><path d="M4 7l6-5 6 5"/></svg>
    <h3>Rental<br>fleet</h3><p>Well kept trainers ready to fly</p>
  </div>
  <div class="arrows" style="left:572px;top:1484px">
    <svg viewBox="0 0 22 12" fill="none" stroke="#1d1d3a" stroke-width="1.4"><path d="M22 6H2M6 1L1 6l5 5"/></svg>
    <svg viewBox="0 0 22 12" fill="none" stroke="#1d1d3a" stroke-width="1.4"><path d="M0 6h20M16 1l5 5-5 5"/></svg>
  </div>
</section>

<!-- VIDEO BAND -->
<section>
  <div class="abs" role="img" aria-label="Light aircraft on the apron beside the hangar" style="left:0;top:1518px;width:1200px;height:309px;background:linear-gradient(90deg,#7c6c10,#8f7d12)"></div>
  <svg class="abs" style="left:0;top:1518px" width="1200" height="309" viewBox="0 0 1200 309"><polygon points="729,0 1200,0 1200,309 419,309" fill="#262463"/></svg>
  <div class="abs" style="left:568px;top:1583px;width:62px;height:62px;border-radius:50%;background:#fff"></div>
  <svg class="abs" style="left:591px;top:1602px" width="20" height="24" viewBox="0 0 20 24"><path d="M0 0l20 12L0 24z" fill="#111"/></svg>
  <h2 class="heading center" style="top:1672px;color:#fff;line-height:38px">Tell us about your aircraft and our<br>technicians will send you a quote</h2>
  <div class="btn" style="left:470px;top:1754px;width:123px;height:31px">Book Now</div>
  <div class="btn light" style="left:607px;top:1754px;width:122px;height:31px">Read More</div>
</section>

<!-- FLEET -->
<section>
  <div class="label" style="left:113px;top:1895px">Rental Fleet</div>
  <h2 class="heading" style="left:113px;top:1913px">Browse our<br>rental aircraft</h2>
  <p class="abs" style="left:113px;top:1998px;width:295px;font:400 11.5px/19px var(--sans)">Rent a Korvane 418 or Halvorn Ranger for solo time, cross country trips or training toward your private, instrument and commercial ratings.</p>
  <div class="arrows" style="left:113px;top:2100px">
    <svg viewBox="0 0 22 12" fill="none" stroke="#1d1d3a" stroke-width="1.4"><path d="M22 6H2M6 1L1 6l5 5"/></svg>
    <svg viewBox="0 0 22 12" fill="none" stroke="#1d1d3a" stroke-width="1.4"><path d="M0 6h20M16 1l5 5-5 5"/></svg>
  </div>
  <div class="abs" role="img" aria-label="Faint drawing of a small white aircraft" style="left:48px;top:2150px;width:330px;height:225px;background:radial-gradient(ellipse at center,#f1f1f3 0%,rgba(241,241,243,0) 70%)"></div>

  <div class="charter" style="left:428px;width:252px">
    <div role="img" aria-label="Flight instructor with a student by a trainer aircraft" style="position:absolute;inset:0;background:linear-gradient(180deg,#c7d2e0,#5a6f9c 60%,#2d3d6a)"></div>
    <div class="panel"><div class="tag">Korvane 418</div>
      <ul><li><b>Seats :</b> 4 people</li><li><b>Engine :</b> Single piston</li><li><b>Rate From :</b> $165 / hour</li><li><b>Use :</b> Rental &amp; training</li></ul>
      <div class="btn" style="left:18px;top:144px;width:123px;height:31px">Book Now</div></div>
  </div>
  <div class="charter" style="left:700px;width:251px">
    <div role="img" aria-label="Cockpit seats of a small training aircraft" style="position:absolute;inset:0;background:linear-gradient(180deg,#d7d3cd,#a48f72 55%,#4a3f34)"></div>
    <div class="panel"><div class="tag">Halvorn Ranger</div>
      <ul><li><b>Seats :</b> 4 people</li><li><b>Engine :</b> Single piston</li><li><b>Rate From :</b> $159 / hour</li><li><b>Use :</b> Rental &amp; training</li></ul>
      <div class="btn" style="left:18px;top:144px;width:123px;height:31px">Book Now</div></div>
  </div>
  <div class="charter" style="left:972px;width:228px">
    <div role="img" aria-label="Aircraft wing above the clouds" style="position:absolute;inset:0;background:linear-gradient(180deg,#6f8fc4,#b8c9e3 55%,#e8e6ec)"></div>
    <div class="panel"><div class="tag">Discovery Flight</div>
      <ul><li><b>Time :</b> 1 hour</li><li><b>Aircraft :</b> Korvane 418</li><li><b>Rate From :</b> $129</li><li><b>Person :</b> Student 1</li></ul>
      <div class="btn" style="left:18px;top:144px;width:123px;height:31px">Book Now</div></div>
  </div>
</section>

<!-- REQUEST FORM -->
<section>
  <svg class="abs" style="left:0;top:2261px" width="1200" height="525" viewBox="0 0 1200 525"><polygon points="771,0 1200,0 1200,525 698,525 698,80" fill="#b39a0c"/></svg>
  <div class="abs" style="left:185px;top:2341px;width:830px;height:445px;background:var(--mist)"></div>
  <div class="label center" style="top:2379px">Get Started</div>
  <h2 class="heading center" style="top:2399px">Request service or a lesson</h2>
  <div class="field" style="left:234px;top:2457px;width:356px">Your Name</div>
  <div class="field" style="left:602px;top:2457px;width:356px">Aircraft Model</div>
  <div class="field" style="left:234px;top:2541px;width:356px">Select Date</div>
  <div class="field" style="left:602px;top:2541px;width:169px">Select time</div>
  <div class="field" style="left:784px;top:2541px;width:174px">Service<svg width="13" height="8" viewBox="0 0 13 8" fill="none" stroke="#1d1d3a" stroke-width="1.4"><path d="M1 1l5.5 5.5L12 1"/></svg></div>
  <div class="field" style="left:234px;top:2624px;width:724px">Select Repair, Rental or Flight Training<svg width="13" height="8" viewBox="0 0 13 8" fill="none" stroke="#1d1d3a" stroke-width="1.4"><path d="M1 1l5.5 5.5L12 1"/></svg></div>
  <p class="abs" style="left:234px;top:2726px;font:400 6.5px/1 var(--sans);color:#8a8a96">* After sending your request, we'll contact you with more details and times.</p>
  <div class="btn" style="left:539px;top:2714px;width:122px;height:32px">Book Now</div>
</section>

<!-- TESTIMONIALS -->
<section>
  <div class="abs" style="left:0;top:2786px;width:1200px;height:344px;background:var(--navy)"></div>
  <div class="label" style="left:113px;top:2870px">Customers Feedback</div>
  <h2 class="heading" style="left:113px;top:2887px;color:#fff">What pilots<br>are saying<br>about us</h2>
  <div class="arrows" style="left:113px;top:3016px">
    <svg viewBox="0 0 22 12" fill="none" stroke="#fff" stroke-width="1.4"><path d="M22 6H2M6 1L1 6l5 5"/></svg>
    <svg viewBox="0 0 22 12" fill="none" stroke="#fff" stroke-width="1.4"><path d="M0 6h20M16 1l5 5-5 5"/></svg>
  </div>

  <div class="review" style="left:421px">
    <div class="avatar" role="img" aria-label="Customer portrait" style="background:#b9c3d3"></div>
    <div class="quote">”</div>
    <h4>Aaron Pell</h4><small>Aircraft Owner</small>
    <p>Every annual is explained in detail and my turboprop has flown far more smoothly between inspections. The shop treats safety as the real priority.</p>
    <div class="stars">
      <svg width="12" height="12" viewBox="0 0 12 12"><path d="M6 0l1.8 3.8 4.2.5-3.1 2.9.8 4.1L6 9.3 2.3 11.3l.8-4.1L0 4.3l4.2-.5z" fill="#b39a0c"/></svg>
      <svg width="12" height="12" viewBox="0 0 12 12"><path d="M6 0l1.8 3.8 4.2.5-3.1 2.9.8 4.1L6 9.3 2.3 11.3l.8-4.1L0 4.3l4.2-.5z" fill="#b39a0c"/></svg>
      <svg width="12" height="12" viewBox="0 0 12 12"><path d="M6 0l1.8 3.8 4.2.5-3.1 2.9.8 4.1L6 9.3 2.3 11.3l.8-4.1L0 4.3l4.2-.5z" fill="#b39a0c"/></svg>
      <svg width="12" height="12" viewBox="0 0 12 12"><path d="M6 0l1.8 3.8 4.2.5-3.1 2.9.8 4.1L6 9.3 2.3 11.3l.8-4.1L0 4.3l4.2-.5z" fill="#b39a0c"/></svg>
      <svg width="12" height="12" viewBox="0 0 12 12"><path d="M6 0l1.8 3.8 4.2.5-3.1 2.9.8 4.1L6 9.3 2.3 11.3l.8-4.1L0 4.3l4.2-.5z" fill="#b39a0c"/></svg>
    </div>
  </div>
  <div class="review" style="left:765px">
    <div class="avatar" role="img" aria-label="Customer portrait" style="background:#c8cdd6"></div>
    <div class="quote">”</div>
    <h4>Mara Quist</h4><small>Student Pilot</small>
    <p>I earned my private pilot license here and now I am working on my instrument rating. The instructors are patient and the rental aircraft are spotless.</p>
    <div class="stars">
      <svg width="12" height="12" viewBox="0 0 12 12"><path d="M6 0l1.8 3.8 4.2.5-3.1 2.9.8 4.1L6 9.3 2.3 11.3l.8-4.1L0 4.3l4.2-.5z" fill="#b39a0c"/></svg>
      <svg width="12" height="12" viewBox="0 0 12 12"><path d="M6 0l1.8 3.8 4.2.5-3.1 2.9.8 4.1L6 9.3 2.3 11.3l.8-4.1L0 4.3l4.2-.5z" fill="#b39a0c"/></svg>
      <svg width="12" height="12" viewBox="0 0 12 12"><path d="M6 0l1.8 3.8 4.2.5-3.1 2.9.8 4.1L6 9.3 2.3 11.3l.8-4.1L0 4.3l4.2-.5z" fill="#b39a0c"/></svg>
      <svg width="12" height="12" viewBox="0 0 12 12"><path d="M6 0l1.8 3.8 4.2.5-3.1 2.9.8 4.1L6 9.3 2.3 11.3l.8-4.1L0 4.3l4.2-.5z" fill="#b39a0c"/></svg>
      <svg width="12" height="12" viewBox="0 0 12 12"><path d="M6 0l1.8 3.8 4.2.5-3.1 2.9.8 4.1L6 9.3 2.3 11.3l.8-4.1L0 4.3l4.2-.5z" fill="#b39a0c"/></svg>
    </div>
  </div>
</section>

<!-- BLOG -->
<section>
  <div class="label center" style="top:3181px">From the Blog Posts</div>
  <h2 class="heading center" style="top:3201px">Checkout latest hangar<br>and flight school news</h2>

  <article class="post" style="left:185px">
    <div role="img" aria-label="Light aircraft inside a hangar" style="position:absolute;left:0;top:0;width:262px;height:205px;background:linear-gradient(180deg,#5e5e62,#a4a4a2 55%,#4a4a4c)"></div>
    <div class="pill">24 Jan</div>
    <div class="meta"><span><svg width="12" height="12" viewBox="0 0 12 12"><circle cx="6" cy="6" r="6" fill="#b39a0c"/></svg>Avery</span><span><svg width="13" height="12" viewBox="0 0 13 12"><path d="M1 1h11v7H5l-3 3V8H1z" fill="#b39a0c"/></svg>2 Comments</span></div>
    <h3>What a thorough annual inspection should include</h3>
    <div class="more">Read More<svg width="22" height="10" viewBox="0 0 22 10" fill="none" stroke="#8a8a96" stroke-width="1.3"><path d="M0 5h20M16 1l4 4-4 4"/></svg></div>
  </article>
  <article class="post" style="left:469px">
    <div role="img" aria-label="Instrument panel in a training aircraft cockpit" style="position:absolute;left:0;top:0;width:262px;height:205px;background:linear-gradient(180deg,#8f95a0,#3a3d46 45%,#1b1c22)"></div>
    <div class="pill">24 Jan</div>
    <div class="meta"><span><svg width="12" height="12" viewBox="0 0 12 12"><circle cx="6" cy="6" r="6" fill="#b39a0c"/></svg>Avery</span><span><svg width="13" height="12" viewBox="0 0 13 12"><path d="M1 1h11v7H5l-3 3V8H1z" fill="#b39a0c"/></svg>2 Comments</span></div>
    <h3>A first-time student's guide to the private pilot license</h3>
    <div class="more">Read More<svg width="22" height="10" viewBox="0 0 22 10" fill="none" stroke="#8a8a96" stroke-width="1.3"><path d="M0 5h20M16 1l4 4-4 4"/></svg></div>
  </article>
  <article class="post" style="left:753px">
    <div role="img" aria-label="Trainer aircraft parked on the ramp" style="position:absolute;left:0;top:0;width:262px;height:205px;background:linear-gradient(180deg,#a9b3c0,#6b6f78 50%,#3d3f46)"></div>
    <div class="pill">24 Jan</div>
    <div class="meta"><span><svg width="12" height="12" viewBox="0 0 12 12"><circle cx="6" cy="6" r="6" fill="#b39a0c"/></svg>Avery</span><span><svg width="13" height="12" viewBox="0 0 13 12"><path d="M1 1h11v7H5l-3 3V8H1z" fill="#b39a0c"/></svg>2 Comments</span></div>
    <h3>Renting an aircraft everything you need to know about cost</h3>
    <div class="more">Read More<svg width="22" height="10" viewBox="0 0 22 10" fill="none" stroke="#8a8a96" stroke-width="1.3"><path d="M0 5h20M16 1l4 4-4 4"/></svg></div>
  </article>
</section>

<!-- FOOTER -->
<footer class="footer">
  <div class="brand" style="left:113px;top:70px"><i></i>SKYLARK AIR WORKS</div>
  <p class="abs" style="left:113px;top:149px;width:300px;font:600 13.5px/19px var(--sans);color:#fff">Quality flying is safe flying. Repairs, rental and flight training.</p>
  <h5 style="left:518px;top:52px">Explore</h5>
  <ul style="left:518px;top:82px"><li>About</li><li>Maintenance &amp; Repairs</li><li>Aircraft Rental</li><li>Flight School</li><li>Book a Lesson</li></ul>
  <h5 style="left:703px;top:52px">Links</h5>
  <ul style="left:703px;top:82px"><li>Terms of Use</li><li>Contact Us</li><li>News &amp; Press</li><li>Faqs</li></ul>
  <h5 style="left:857px;top:52px">Contact</h5>
  <ul style="left:857px;top:82px;line-height:21px">
    <li><svg width="12" height="12" viewBox="0 0 12 12"><path d="M2.5 0.5l2 2.5-1.2 1.6a7 7 0 004 4l1.6-1.2 2.5 2-1.2 2C5 11.5 0.5 7 0.5 1.7z" fill="#b39a0c"/></svg>+1 (555) 014 - 2288</li>
    <li><svg width="12" height="10" viewBox="0 0 12 10"><rect width="12" height="10" rx="1" fill="#b39a0c"/><path d="M0.5 1l5.5 4.5L11.5 1" fill="none" stroke="#1a1a4f" stroke-width="1"/></svg>hello@skylarkair.com</li>
    <li><svg width="12" height="14" viewBox="0 0 12 14"><path d="M6 0a6 6 0 016 6c0 4-6 8-6 8S0 10 0 6a6 6 0 016-6z" fill="#b39a0c"/><circle cx="6" cy="6" r="2.2" fill="#1a1a4f"/></svg>Lawrenceville, Georgia</li>
  </ul>
  <div class="abs" style="left:113px;top:211px;width:974px;height:1px;background:rgba(255,255,255,.2)"></div>
  <p class="abs" style="left:0;top:235px;width:1200px;text-align:center;font:400 11px/1 var(--sans);color:#fff">© Copyright 2023 by Skylark Air Works</p>
</footer>

</div>
</body>
</html>
```